Summer Special for Harbourline Gym

Running a 12 month special starting from 1st Jan 2019. I already have the image (see below), I just need the font and layout to have a summer feel and to be eye catching. Format required is for a Facebook cover, Instagram, if possible the one image but spread across 3 tiles on the homepage and a format for a poster .

"SUMMER SPECIAL
12 months from
$350.00
SAVE OVER 20%"
"Terms and conditions apply"

Attached is the photo for the current promo, a logo we generally use and another special we have run in the past to assist you

Target Market(s)

18 - 45 male and female

Industry/Entity Type

Fitness

Font styles to use
Sans Serif
Script

Colors

Designer to choose colors to be used in the design.

Requirements
Must have
• The main emphasis would be on the Summer font/text (special) and the layout of the text. If we can add some brighter colors to the layout that would be great just to capture their attention. If there's any effects you want to add to it that would be great. The logo can be faint in the background.
• "SUMMER SPECIAL
• 12 months from
• $350.00
• SAVE OVER 20%"
• "Terms and conditions apply"
• All contact details, address, website, etc which will be supplied
Nice to have
• Some artistic effects to catch your eye and enhance the professionalism of the designer

```html
<!DOCTYPE html>
<html lang="en">
<head>
<meta charset="utf-8">
<title>Summer Special – Harbourline Gym</title>
<link rel="stylesheet" href="https://fonts.googleapis.com/css2?family=Open+Sans:wght@400;700;800&display=swap">
<style>
  :root{
    --board:#dcdcdc;
    --sun:#f6d21a;
    --sky:#2fd3e8;
    --ink:#000000;
    --mist:#c9d3d4;
    --red:#e31b2e;
    --red-soft:#e33646;
    --price:#f35863;
    --gold:#f6d21a;
    --white:#ffffff;
    --faint-gold:#c9a91a;
    --faint-gold-text:#e8c417;
    --logo-box:#050505;
  }
  html,body{margin:0;padding:0;width:1158px;height:1200px;overflow:hidden}
  body{
    background:radial-gradient(ellipse at 50% 50%, #ececec 0%, var(--board) 60%, #c9c9c9 100%);
    font-family:"Open Sans", Arial, sans-serif;
    position:relative;
  }
  .banner{
    position:absolute;
    display:block;
    filter:drop-shadow(0 22px 26px rgba(0,0,0,.38));
  }
  .banner--photo-bright{left:148px;top:14px;width:848px;height:312px}
  .banner--type-only{left:148px;top:424px;width:848px;height:312px}
  .banner--dark{left:142px;top:862px;width:849px;height:312px}
  .contact{font-family:"Open Sans", Arial, sans-serif;font-weight:700;fill:var(--white)}
  .contact--web{font-size:16.5px}
  .contact--address{font-size:12.5px}
  .headline{font-family:"Open Sans", Arial, sans-serif;font-weight:800;fill:var(--gold);letter-spacing:-1px}
  .subline{font-family:"Open Sans", Arial, sans-serif;font-weight:800;fill:var(--ink);font-size:20px}
  .price{font-family:"Open Sans", Arial, sans-serif;font-weight:700;fill:var(--white);font-size:38px;letter-spacing:-1.5px}
  .save-top{font-family:"Open Sans", Arial, sans-serif;font-weight:400;fill:var(--white);font-size:17px}
  .save-bottom{font-family:"Open Sans", Arial, sans-serif;font-weight:700;fill:var(--white);font-size:17px}
  .terms{font-family:"Open Sans", Arial, sans-serif;font-weight:400;fill:var(--ink);font-size:11.5px}
  .brand-name{font-family:"Open Sans", Arial, sans-serif;font-weight:800}
  .brand-name--faint{font-size:10px;fill:var(--faint-gold-text)}
  .brand-name--dark{font-size:16px;fill:var(--white)}
  .c-sun{fill:var(--sun)} .c-sky{fill:var(--sky)} .c-ink{fill:var(--ink)} .c-mist{fill:var(--mist)}
  .c-red{fill:var(--red)} .c-red-soft{fill:var(--red-soft)} .c-price{fill:var(--price)}
  .c-white{fill:var(--white)}
  .dash{stroke:var(--white);stroke-width:5;stroke-dasharray:22 13;fill:none}
</style>
</head>
<body>

<!-- Banner one: bright colours with athlete photo -->
<svg class="banner banner--photo-bright" viewBox="0 0 1060 390" xmlns="http://www.w3.org/2000/svg">
  <defs>
    <linearGradient id="athleteToneA" x1="0" y1="0" x2="0" y2="1">
      <stop offset="0" stop-color="#3a2a22"/>
      <stop offset="0.25" stop-color="#8a5a40"/>
      <stop offset="0.65" stop-color="#9c6448"/>
      <stop offset="0.75" stop-color="#d0624c"/>
      <stop offset="1" stop-color="#c85a46"/>
    </linearGradient>
  </defs>
  <rect class="c-sky" width="1060" height="390"/>
  <polygon class="c-sun" points="0,0 1060,0 0,390"/>
  <line class="dash" x1="40" y1="362" x2="1015" y2="6"/>
  <rect x="712" y="12" width="348" height="378" fill="url(#athleteToneA)" role="img" aria-label="Photo of a muscular athlete in a cap and red shorts"/>
  <text class="contact contact--web" x="72" y="40">hello@harbourlinegym.com.au</text>
  <text class="contact contact--web" x="72" y="61">www.harbourlinegym.com.au</text>
  <g opacity="0.55">
    <circle cx="167" cy="115" r="44" fill="var(--faint-gold)"/>
    <text class="brand-name brand-name--faint" x="167" y="113" text-anchor="middle">HARBOURLINE</text>
    <text class="brand-name brand-name--faint" x="167" y="126" text-anchor="middle">GYM</text>
  </g>
  <text class="contact contact--address" x="167" y="177" text-anchor="middle">14 Wharf Road,</text>
  <text class="contact contact--address" x="167" y="193" text-anchor="middle">Portside Victoria 3099</text>
  <text class="contact contact--address" x="167" y="209" text-anchor="middle">9555 0182</text>
  <circle class="c-red" cx="490" cy="185" r="180"/>
  <circle class="c-red-soft" cx="490" cy="185" r="160"/>
  <text class="headline" x="488" y="165" text-anchor="middle" font-size="52">SUMMER</text>
  <text class="headline" x="488" y="212" text-anchor="middle" font-size="54">SPECIAL</text>
  <text class="subline" x="492" y="235" text-anchor="middle">12 MONTHS FROM</text>
  <circle class="c-price" cx="487" cy="289" r="47"/>
  <text class="price" x="487" y="302" text-anchor="middle">$350</text>
  <g>
    <circle class="c-white" cx="641" cy="65" r="55"/>
    <polygon class="c-white" points="608,98 648,114 624,148"/>
    <circle class="c-sky" cx="641" cy="65" r="49"/>
    <polygon class="c-sky" points="614,100 642,110 628,138"/>
    <text class="save-top" x="640" y="61" text-anchor="middle">SAVE</text>
    <text class="save-bottom" x="641" y="78" text-anchor="middle">OVER 20%</text>
  </g>
  <text class="terms" x="493" y="378" text-anchor="middle">Terms and conditions apply*</text>
</svg>

<!-- Banner two: bright colours, type only -->
<svg class="banner banner--type-only" viewBox="0 0 1060 390" xmlns="http://www.w3.org/2000/svg">
  <rect class="c-sky" width="1060" height="390"/>
  <polygon class="c-sun" points="0,0 1060,0 0,390"/>
  <line class="dash" x1="40" y1="362" x2="1015" y2="6"/>
  <text class="contact contact--web" x="80" y="48">hello@harbourlinegym.com.au</text>
  <text class="contact contact--web" x="80" y="69">www.harbourlinegym.com.au</text>
  <g opacity="0.55">
    <circle cx="168" cy="137" r="44" fill="var(--faint-gold)"/>
    <text class="brand-name brand-name--faint" x="168" y="135" text-anchor="middle">HARBOURLINE</text>
    <text class="brand-name brand-name--faint" x="168" y="148" text-anchor="middle">GYM</text>
  </g>
  <text class="contact contact--address" x="168" y="213" text-anchor="middle">14 Wharf Road,</text>
  <text class="contact contact--address" x="168" y="229" text-anchor="middle">Portside Victoria 3099</text>
  <text class="contact contact--address" x="168" y="245" text-anchor="middle">9555 0182</text>
  <circle class="c-red" cx="527" cy="180" r="180"/>
  <circle class="c-red-soft" cx="527" cy="180" r="160"/>
  <text class="headline" x="525" y="161" text-anchor="middle" font-size="52">SUMMER</text>
  <text class="headline" x="525" y="208" text-anchor="middle" font-size="54">SPECIAL</text>
  <text class="subline" x="530" y="231" text-anchor="middle">12 MONTHS FROM</text>
  <circle class="c-price" cx="525" cy="287" r="47"/>
  <text class="price" x="525" y="300" text-anchor="middle">$350</text>
  <g>
    <circle class="c-white" cx="677" cy="58" r="55"/>
    <polygon class="c-white" points="644,91 684,107 660,141"/>
    <circle class="c-sky" cx="677" cy="58" r="49"/>
    <polygon class="c-sky" points="650,93 678,103 664,131"/>
    <text class="save-top" x="676" y="54" text-anchor="middle">SAVE</text>
    <text class="save-bottom" x="677" y="71" text-anchor="middle">OVER 20%</text>
  </g>
  <text class="terms" x="531" y="375" text-anchor="middle">Terms and conditions apply*</text>
</svg>

<!-- Banner three: dark variant with athlete photo -->
<svg class="banner banner--dark" viewBox="0 0 1061 390" xmlns="http://www.w3.org/2000/svg">
  <defs>
    <linearGradient id="athleteToneB" x1="0" y1="0" x2="0" y2="1">
      <stop offset="0" stop-color="#2c2522"/>
      <stop offset="0.25" stop-color="#8a5a40"/>
      <stop offset="0.65" stop-color="#a06a4e"/>
      <stop offset="0.75" stop-color="#d0624c"/>
      <stop offset="1" stop-color="#c65c48"/>
    </linearGradient>
  </defs>
  <rect class="c-mist" width="1061" height="390"/>
  <polygon class="c-ink" points="0,0 1061,0 0,390"/>
  <line class="dash" x1="40" y1="360" x2="1012" y2="6"/>
  <rect x="738" y="12" width="323" height="378" fill="url(#athleteToneB)" role="img" aria-label="Photo of a muscular athlete in a cap and red shorts"/>
  <rect x="31" y="66" width="290" height="184" fill="var(--logo-box)"/>
  <text class="contact contact--web" x="79" y="37">hello@harbourlinegym.com.au</text>
  <text class="contact contact--web" x="79" y="58">www.harbourlinegym.com.au</text>
  <circle cx="166" cy="148" r="68" fill="none" stroke="var(--white)" stroke-width="3"/>
  <text class="brand-name brand-name--dark" x="166" y="145" text-anchor="middle">HARBOURLINE</text>
  <text class="brand-name brand-name--dark" x="166" y="165" text-anchor="middle">GYM</text>
  <text class="contact contact--address" x="166" y="237" text-anchor="middle">14 Wharf Road,</text>
  <text class="contact contact--address" x="166" y="253" text-anchor="middle">Portside Victoria 3099</text>
  <text class="contact contact--address" x="166" y="269" text-anchor="middle">9555 0182</text>
  <circle class="c-red" cx="526" cy="178" r="180"/>
  <circle class="c-red-soft" cx="526" cy="178" r="160"/>
  <text class="headline" x="528" y="152" text-anchor="middle" font-size="60">SUMMER</text>
  <text class="headline" x="528" y="207" text-anchor="middle" font-size="62">SPECIAL</text>
  <text class="subline" x="530" y="231" text-anchor="middle">12 MONTHS FROM</text>
  <circle class="c-price" cx="524" cy="287" r="47"/>
  <text class="price" x="524" y="300" text-anchor="middle">$350</text>
  <g>
    <circle class="c-white" cx="700" cy="57" r="55"/>
    <polygon class="c-white" points="667,90 707,106 683,140"/>
    <circle class="c-sky" cx="700" cy="57" r="49"/>
    <polygon class="c-sky" points="673,92 701,102 687,130"/>
    <text class="save-top" x="699" y="53" text-anchor="middle">SAVE</text>
    <text class="save-bottom" x="700" y="70" text-anchor="middle">OVER 20%</text>
  </g>
  <text class="terms" x="531" y="374" text-anchor="middle">Terms and conditions apply*</text>
</svg>

</body>
</html>
```